Facebook Header Design Project.

I'm supplying white and colored logos. The Facebook page already exists. URL = https://www.pagebook.example/lumocrest.design The design should not be based on what's already there. Consider mobile implications of the design. This Design will form the designs of other social media headers. LumoCrest is a web design | digital marketing company.

Target Market(s)

People interested in web design | digital marketing services.

Industry/Entity Type

LumoCrest is a web design | digital marketing company. That should be clear in the design.

Colors
0054AA
0677BA
7BADD7
CADEEF
E8F1F8

Requirements
Must have
• Logo. Use Facebook header image dimension.
Nice to have
• Use a color scheme like the logo and feel free to add a color or two from the other side of the color whee.

```html
<!DOCTYPE html>
<html lang="en">
<head>
<meta charset="utf-8">
<title>LumoCrest — Page Header</title>
<link rel="stylesheet" href="https://fonts.googleapis.com/css2?family=Exo+2:ital,wght@0,700;1,400;1,700;1,800&display=swap">
<style>
  :root {
    --brand-deep: #0054AA;
    --brand-mid: #0677BA;
    --brand-soft: #7BADD7;
    --brand-pale: #CADEEF;
    --brand-mist: #E8F1F8;
    --white: #FFFFFF;
  }
  * { margin: 0; padding: 0; box-sizing: border-box; }
  html, body {
    width: 1200px;
    height: 457px;
    overflow: hidden;
    background: var(--white);
  }
  .header-banner {
    position: relative;
    width: 1200px;
    height: 457px;
    overflow: hidden;
    font-family: "Exo 2", sans-serif;
  }
  .city-backdrop {
    position: absolute;
    inset: 0;
    background:
      radial-gradient(ellipse at 70% 50%, var(--white) 0%, rgba(255,255,255,0.6) 35%, rgba(255,255,255,0) 70%),
      linear-gradient(180deg, var(--brand-pale) 0%, var(--brand-mist) 55%, var(--brand-pale) 100%);
  }
  .phone-illustration {
    position: absolute;
    left: 88px;
    top: 24px;
    width: 356px;
    height: 420px;
    border-radius: 40px;
    background: linear-gradient(160deg, var(--brand-soft) 0%, var(--brand-mid) 55%, var(--brand-deep) 100%);
    opacity: 0.85;
  }
  .brand-block {
    position: absolute;
    left: 520px;
    top: 50px;
  }
  .brand-name {
    font-weight: 700;
    font-style: normal;
    font-size: 86px;
    line-height: 1;
    color: var(--brand-deep);
    letter-spacing: 0.5px;
  }
  .tagline {
    position: absolute;
    left: 520px;
    top: 212px;
    font-style: italic;
    text-transform: uppercase;
    line-height: 1;
  }
  .tagline-intro {
    display: block;
    font-weight: 400;
    font-size: 30px;
    color: var(--brand-mid);
    letter-spacing: 1px;
  }
  .tagline-primary {
    display: block;
    margin-top: 8px;
    font-weight: 800;
    font-size: 62px;
    color: var(--brand-deep);
    letter-spacing: 1px;
  }
  .tagline-secondary {
    display: block;
    margin-top: 6px;
    font-weight: 800;
    font-size: 34px;
    color: var(--brand-deep);
    letter-spacing: 1px;
  }
  .tagline-tertiary {
    display: block;
    margin-top: 4px;
    font-weight: 800;
    font-size: 34px;
    color: var(--brand-deep);
    letter-spacing: 1px;
  }
</style>
</head>
<body>
  <main class="header-banner">
    <div class="city-backdrop" role="img" aria-label="Faint pale-blue city skyline with a network of connected lines"></div>

    <div class="phone-illustration" role="img" aria-label="Illustration of a smartphone showing charts, a magnifying glass and a megaphone, symbolising digital marketing"></div>

    <div class="brand-block">
      <h1 class="brand-name">LumoCrest</h1>
    </div>

    <p class="tagline">
      <span class="tagline-intro">LumoCrest is a</span>
      <span class="tagline-primary">Web Design</span>
      <span class="tagline-secondary">Digital Marketing</span>
      <span class="tagline-tertiary">Company</span>
    </p>
  </main>
</body>
</html>
```